Organic rose water based skincare line in need of product label and packaging design

We are looking for a simple, clean, modern labeling and packaging design for 2 of our products. Our brand's demographic is upscale females ages 20-40. We want our packaging to be very minimalistic, and instagramable.

Product #1: Rose water facial spray "Lumi Mist"
Product #2: Rose water facial toner "Velvet Hush Hour"

Please see attached images for our current logo and label design. We have also added some images that inspire our branding.

Target Market(s)

trendy woman ages 20-40

Industry/Entity Type

Skin Care Product

Font styles to use
Serif
Sans Serif

Colors

Designer to choose only greyscale colors for use in the design.

Requirements
Must have
• Must have our logo, bottle size, product name on front and how to use and ingredient on the back. Please see project description and attached images for more information.
Should not have
• Too much going on or too many colors.

```html
<!DOCTYPE html>
<html lang="en">
<head>
<meta charset="utf-8">
<title>the petal house — Velvet Hush Hour &amp; Lumi Mist packaging</title>
<link rel="stylesheet" href="https://fonts.googleapis.com/css2?family=Roboto+Condensed:wght@300;700&family=Roboto:wght@300;400&display=swap">
<style>
  :root {
    --page-bg: #e4e7e8;
    --ink: #0b0b0b;
    --paper: #ffffff;
    --muted: #e6e6e6;
    --art-light: #8a8a8a;
    --art-dark: #2a2a2a;
  }
  * { box-sizing: border-box; margin: 0; padding: 0; }
  html, body { width: 1200px; height: 960px; overflow: hidden; }
  body {
    background: var(--page-bg);
    font-family: "Roboto", Arial, sans-serif;
    color: var(--paper);
    position: relative;
  }
  .box-front {
    position: absolute;
    left: 130px; top: 70px;
    width: 290px; height: 820px;
    background: var(--ink);
  }
  .label {
    position: absolute;
    top: 240px;
    width: 300px; height: 400px;
    background: var(--ink);
    border-radius: 6px;
  }
  .label--toner { left: 490px; }
  .label--mist { left: 830px; }

  .brand-name {
    position: absolute;
    font-family: "Roboto", Arial, sans-serif;
    font-weight: 400;
    color: var(--paper);
    white-space: nowrap;
    letter-spacing: 0.02em;
  }
  .rose-art {
    position: absolute;
    border-radius: 40% 40% 12% 12%;
    background: linear-gradient(180deg, var(--art-light) 0%, var(--art-dark) 100%);
    opacity: 0.85;
  }
  .product-title {
    position: absolute;
    font-family: "Roboto Condensed", Arial, sans-serif;
    font-weight: 300;
    text-transform: uppercase;
    line-height: 1.02;
    color: var(--paper);
  }
  .product-title strong { font-weight: 700; display: block; }
  .product-title span { display: block; }
  .descriptor {
    position: absolute;
    left: 0; right: 0;
    text-align: center;
    font-weight: 300;
    line-height: 1.3;
    color: var(--muted);
  }
  .volume {
    position: absolute;
    left: 0; right: 0;
    text-align: center;
    font-weight: 400;
    color: var(--paper);
  }

  /* box front */
  .box-front .brand-name { left: 34px; top: 150px; font-size: 19px; }
  .box-front .rose-art { left: 205px; top: 140px; width: 75px; height: 230px; }
  .box-front .product-title { left: 34px; top: 270px; font-size: 42px; }
  .box-front .descriptor { top: 540px; font-size: 18px; }
  .box-front .volume { top: 740px; font-size: 17px; }

  /* bottle labels */
  .label .brand-name { left: 28px; top: 44px; font-size: 17px; }
  .label .rose-art { left: 180px; top: 28px; width: 80px; height: 170px; }
  .label .product-title { left: 28px; top: 150px; font-size: 40px; }
  .label .descriptor { top: 290px; font-size: 16px; }
  .label .volume { top: 350px; font-size: 15px; }
</style>
</head>
<body>

  <section class="box-front" aria-label="Velvet Hush Hour carton front">
    <p class="brand-name">the petal house</p>
    <div class="rose-art" role="img" aria-label="Line drawing of a single long-stem rose"></div>
    <h1 class="product-title"><span>Velvet</span><strong>Hush</strong><span>Hour</span></h1>
    <p class="descriptor">Organic Rose<br>Facial Toner</p>
    <p class="volume">4 oz / 120ml</p>
  </section>

  <section class="label label--toner" aria-label="Velvet Hush Hour bottle label">
    <p class="brand-name">the petal house</p>
    <div class="rose-art" role="img" aria-label="Line drawing of a single long-stem rose"></div>
    <h2 class="product-title"><span>Velvet</span><strong>Hush</strong><span>Hour</span></h2>
    <p class="descriptor">Organic Rose<br>Facial Toner</p>
    <p class="volume">4 oz / 120ml</p>
  </section>

  <section class="label label--mist" aria-label="Lumi Mist bottle label">
    <p class="brand-name">the petal house</p>
    <div class="rose-art" role="img" aria-label="Line drawing of a single long-stem rose"></div>
    <h2 class="product-title"><span>Lumi</span><strong>Mist</strong></h2>
    <p class="descriptor">Organic Rosewater<br>Hydrating Spray</p>
    <p class="volume">4 oz / 120ml</p>
  </section>

</body>
</html>
```